Professional website for psychological services

Create a professional, easy to navigate website using soothing coastal images and incorporate company logo in design. Website is for a small private clinic that provides psychological services and must be appealing to professional men and women. A website I really like is www.veltoriparc.com I would love something like similar.

Target Market(s)

Professional men and women seeking psychological services

Industry/Entity Type

Mental Health

Number of Pages Required

5+ page

Requirements
Must have
• The website must incorporate the logo provided. The name of the company/website is Brimwell Harbor Renewal Aftercare. Colors must compliment the logo, must be coastal and soothing yet very professional. I would like a website like www.veltoriparc.com
• Pages will be:Home, Services, FAQ and Contact Us. The images included of the building and office are for the contact us page. Under the tab Servies: Individual Psychotherapy, Family Therapy, EMDR I will provide specific content for each.
Nice to have
• I want the website to be easy to navigate and the font easy to read. The writing on the logo is very light and I'm open to changing it slightly if it will be better aesthetically.
Should not have
• Please no pictures of any swimsuits, alcoholic beverages, etc. This is a professional psychological clinic.

```html
<!DOCTYPE html>
<html lang="en">
<head>
<meta charset="utf-8">
<title>Brimwell Harbor Renewal Aftercare</title>
<link rel="stylesheet" href="https://fonts.googleapis.com/css2?family=Open+Sans:wght@400;600;700&family=Roboto:wght@400;500&family=Raleway:ital,wght@1,400&family=Indie+Flower&display=swap">
<style>
:root{
  --sky:#4fb0f3;
  --ink:#222;
  --muted:#777;
  --white:#fff;
  --hero-top:#b98a5c;
  --hero-bottom:#3f8c9c;
  --sea:#0c5f80;
  --sea-soft:#1a7a95;
  --sea-deep:#0a4f6e;
}
*{box-sizing:border-box;margin:0;padding:0}
html,body{width:1200px;height:3593px;overflow:hidden}
body{position:relative;background:var(--white);font-family:"Roboto",sans-serif;color:var(--ink)}
.abs{position:absolute}
.script{font-family:"Indie Flower",cursive;color:var(--sky);font-weight:400}

/* hero */
.hero{left:0;top:0;width:1200px;height:640px;background:linear-gradient(180deg,var(--hero-top) 0%,var(--hero-bottom) 100%)}
.nav{top:60px;display:flex;gap:32px;font-family:"Open Sans",sans-serif;font-weight:600;font-size:15px;color:var(--white)}
.nav a{color:inherit;text-decoration:none}
.nav-left{left:106px}
.nav-right{right:106px}
.brand{left:0;width:1200px;text-align:center;color:var(--white);font-family:"Open Sans",sans-serif;font-weight:400}
.brand-hero{top:70px}
.brand-hero .name{display:block;font-size:42px;line-height:52px;margin-top:6px}
.brand-hero .tag{display:block;font-size:11px;letter-spacing:2px;margin-top:20px}
.brand-mark{display:block;width:40px;height:40px;border-radius:50%;background:var(--white);margin:0 auto}

/* about */
.about-photo{left:150px;top:712px;width:316px;height:316px;border-radius:50%;border:14px solid var(--sky);
  background:linear-gradient(160deg,#b99884,#5f7a5c)}
.about-title{left:586px;top:712px;font-size:50px;line-height:60px}
.about-text{left:587px;top:792px;width:520px;font-size:15px;line-height:45px;color:#333}

/* services */
.section-title{left:0;width:1200px;text-align:center;font-size:50px;line-height:60px}
.services-band{left:0;top:1449px;width:1200px;height:440px;background:var(--sky)}
.accent-dot{left:414px;top:1212px;width:72px;height:72px;border-radius:50%;background:var(--sky)}
.service-card{top:1250px;width:304px;background:var(--white);box-shadow:0 6px 16px rgba(0,0,0,.15)}
.service-photo{height:197px}
.service-label{height:50px;line-height:50px;text-align:center;font-family:"Open Sans",sans-serif;font-weight:600;font-size:19px;color:var(--sky)}
.laptop{left:366px;top:1600px;width:464px;height:310px;background:var(--white);border-radius:14px;box-shadow:0 14px 30px rgba(0,0,0,.2);padding:18px}
.laptop-screen{width:100%;height:100%;background:linear-gradient(120deg,#8a8580 0%,#cfc4ba 55%,#b3c6dc 100%);position:relative}
.play{left:50%;top:50%;width:72px;height:72px;margin:-36px 0 0 -36px;border-radius:50%;background:var(--sky)}
.laptop-base{left:312px;top:1910px;width:572px;height:16px;background:#e7e7e7;border-radius:0 0 12px 12px;box-shadow:0 18px 26px rgba(0,0,0,.18)}

/* testimonials */
.quote-card{top:2163px;width:441px;height:213px;border:3px solid #cfe8fb;border-radius:22px;background:var(--white);box-shadow:0 4px 18px rgba(79,176,243,.35);padding:46px 100px 0 88px}
.quote-mark{left:28px;top:14px;font-family:"Open Sans",sans-serif;font-weight:700;font-size:84px;line-height:84px;color:var(--sky)}
.quote-text{font-family:"Raleway",sans-serif;font-style:italic;font-size:13px;line-height:34px;color:#444}
.person{top:2403px;display:flex;align-items:center;gap:22px}
.avatar{width:62px;height:62px;border-radius:50%;border:3px solid #dfe8f0;background:linear-gradient(160deg,#c9c1ba,#6b635d)}
.person-name{font-family:"Open Sans",sans-serif;font-size:17px;color:var(--sky)}
.person-place{font-family:"Open Sans",sans-serif;font-size:13px;color:var(--muted);margin-top:4px}

/* contact */
.contact{left:0;top:2540px;width:1200px;height:1053px;background:linear-gradient(180deg,var(--sea) 0%,var(--sea-soft) 100%)}
.contact-title{color:var(--white);top:2625px}
.field{left:338px;width:517px;height:52px;border-radius:26px;background:var(--white);padding:0 48px;font-family:"Raleway",sans-serif;font-style:italic;font-size:17px;line-height:52px;color:#aaa;box-shadow:0 3px 8px rgba(0,0,0,.2)}
.field-message{height:120px;line-height:40px;padding-top:4px}
.send{left:534px;top:3092px;width:137px;height:36px;border-radius:18px;background:var(--white);text-align:center;line-height:36px;font-family:"Open Sans",sans-serif;font-weight:700;font-size:17px;color:var(--sea-deep)}
.brand-foot{top:3410px}
.brand-foot .name{display:block;font-size:24px;line-height:30px;margin-top:8px}
.brand-foot .tag{display:block;font-size:8px;letter-spacing:1.5px;margin-top:8px}
.socials{left:0;width:1200px;top:3524px;display:flex;justify-content:center;gap:12px}
.socials span{width:16px;height:16px;border-radius:50%;background:rgba(255,255,255,.85)}
.copyright{left:0;width:1200px;top:3568px;text-align:center;font-size:11px;color:var(--white)}
</style>
</head>
<body>

<header class="abs hero" role="img" aria-label="Aerial photo of a sandy beach with waves rolling onto the shore"></header>
<svg class="abs" style="left:0;top:520px" width="1200" height="130" viewBox="0 0 1200 130" aria-hidden="true">
  <path d="M0 60 C120 20 200 100 330 70 C460 40 520 110 640 80 C760 50 820 115 960 78 C1060 52 1130 60 1200 40 L1200 130 L0 130 Z" fill="#fff"/>
</svg>

<nav class="abs nav nav-left"><a href="#">Home</a><a href="#">About us</a><a href="#">Services</a><a href="#">Testimonials</a></nav>
<nav class="abs nav nav-right"><a href="#">Blog</a><a href="#">FAQ</a><a href="#">Appointment</a><a href="#">Contact Us</a></nav>
<div class="abs brand brand-hero"><span class="brand-mark"></span><span class="name">Brimwell Harbor</span><span class="tag">RENEWAL AFTERCARE</span></div>

<section>
  <div class="abs about-photo" role="img" aria-label="Portrait photo of the clinic's psychologist"></div>
  <h2 class="abs script about-title">About us</h2>
  <div class="abs about-text">
    <p>We are a small private clinic that provides psychological services and must be appealing to professional men and women.</p>
    <p>Lorem Ipsum is simply dummy text of the printing and typesetting industry. Lorem Ipsum has been the industry's standard dummy text ever since the 1500s</p>
  </div>
</section>

<section>
  <h2 class="abs script section-title" style="top:1118px">Services</h2>
  <div class="abs services-band"></div>
  <svg class="abs" style="left:0;top:1760px" width="1200" height="130" viewBox="0 0 1200 130" aria-hidden="true">
    <path d="M0 60 C60 10 110 10 160 60 C210 110 250 20 300 60 C340 95 360 100 400 100 L800 100 C850 100 880 30 930 30 C980 30 1000 90 1050 70 C1100 50 1140 10 1200 40 L1200 130 L0 130 Z" fill="#fff"/>
    <path d="M0 90 C60 40 110 50 160 85 C210 120 250 60 300 85" stroke="#a9d8fa" stroke-width="10" fill="none"/>
    <path d="M900 85 C960 50 1010 100 1060 80 C1110 60 1150 50 1200 70" stroke="#a9d8fa" stroke-width="10" fill="none"/>
  </svg>
  <div class="abs accent-dot"></div>
  <article class="abs service-card" style="left:93px">
    <div class="service-photo" role="img" aria-label="Therapist in a session with a client" style="background:linear-gradient(135deg,#e7e2dc,#c2bbb3)"></div>
    <div class="service-label">Individual Psychotherapy</div>
  </article>
  <article class="abs service-card" style="left:448px">
    <div class="service-photo" role="img" aria-label="Family in a group therapy session" style="background:linear-gradient(135deg,#8e827a,#c7bcb0)"></div>
    <div class="service-label">Family Therapy</div>
  </article>
  <article class="abs service-card" style="left:800px">
    <div class="service-photo" role="img" aria-label="Clinician speaking with a patient at a desk" style="background:linear-gradient(135deg,#d9d3cc,#f1eeea)"></div>
    <div class="service-label">EMDR</div>
  </article>
  <div class="abs laptop">
    <div class="laptop-screen" role="img" aria-label="Video still of a client greeting her therapist">
      <span class="abs play"></span>
      <svg class="abs" style="left:50%;top:50%;margin:-14px 0 0 -9px" width="26" height="28" viewBox="0 0 26 28" aria-hidden="true"><path d="M2 1 L25 14 L2 27 Z" fill="#fff"/></svg>
    </div>
  </div>
  <div class="abs laptop-base"></div>
</section>

<section>
  <h2 class="abs script section-title" style="top:2040px">Testimonials</h2>
  <blockquote class="abs quote-card" style="left:79px">
    <span class="abs quote-mark">&ldquo;</span>
    <p class="quote-text">Sed ut perspiciatis unde omnis iste natus error sit voluptatem accusantium doloremque laudantium, totam rem aperiam.</p>
  </blockquote>
  <blockquote class="abs quote-card" style="left:654px">
    <span class="abs quote-mark">&ldquo;</span>
    <p class="quote-text">Sed ut perspiciatis unde omnis iste natus error sit voluptatem accusantium doloremque laudantium, totam rem aperiam.</p>
  </blockquote>
  <div class="abs person" style="left:80px">
    <div class="avatar" role="img" aria-label="Client profile photo"></div>
    <div><div class="person-name">Arlen Whitby</div><div class="person-place">North Atlanta, LA</div></div>
  </div>
  <div class="abs person" style="left:658px">
    <div class="avatar" role="img" aria-label="Client profile photo"></div>
    <div><div class="person-name">Tomas Reyvan</div><div class="person-place">North Atlanta, LA</div></div>
  </div>
</section>

<footer>
  <div class="abs contact" role="img" aria-label="Aerial photo of deep blue ocean meeting a sandy shore"></div>
  <svg class="abs" style="left:0;top:2520px" width="1200" height="110" viewBox="0 0 1200 110" aria-hidden="true">
    <path d="M0 0 L1200 0 L1200 50 C1120 90 1060 20 960 50 C860 80 800 30 690 50 C580 70 520 20 400 55 C290 85 220 30 120 60 C70 75 30 65 0 70 Z" fill="#fff"/>
  </svg>
  <h2 class="abs script section-title contact-title">Contact</h2>
  <div class="abs field" style="top:2722px">Name</div>
  <div class="abs field" style="top:2795px">Email</div>
  <div class="abs field" style="top:2867px">Phone</div>
  <div class="abs field field-message" style="top:2941px">Message</div>
  <div class="abs send">SEND</div>
  <div class="abs brand brand-foot"><span class="brand-mark" style="width:22px;height:22px"></span><span class="name">Brimwell Harbor</span><span class="tag">RENEWAL AFTERCARE</span></div>
  <div class="abs socials"><span></span><span></span><span></span></div>
  <p class="abs copyright">Copyrights 2019. All rights are reserved</p>
</footer>

</body>
</html>
```